Corvant Systems Business Card

Create an appealing and elegant Business card for corvant systems. Include logo and use related colors from website, be creative. Include Business name, my name, tile, address, contacts, address, and social media contacts if possible. Logo PSD file is attached.

Bleed Area: 3.46" x 2.32"
Trim: 3.3" x 2.16"
Safe Area: 3.14" x 2.02"

Save files as vector-based PDF with outlined text and PNG.
No crop marks
CMYK color setting

Business Card Info:

Corvant Systems

Dennis Halvorsen
Owner

512 Brindlemoor Rd Unit C
Ashford Vale, NH 02871
t. 1.888.555.0162
e. dennis.h@corvantsys.example
w. www.corvantsys.example

facebook. www.facebook.com/CorvantSys
twitter. twitter.com/corvantsys
pinterest. www.pinterest.com/corvantsys/

Target Market(s)

Business Owners and Partners

Industry/Entity Type

Business

Requirements
Must have
• Logo and related colors from website

```html
<!DOCTYPE html>
<html lang="en">
<head>
<meta charset="utf-8">
<title>Corvant Systems Business Card</title>
<link rel="stylesheet" href="https://fonts.googleapis.com/css2?family=Open+Sans:wght@400;600;700&display=swap">
<style>
  :root {
    --brand-blue: #4a72b0;
    --ink: #2e2e2e;
    --ink-soft: #4a4a4a;
    --paper: #f4f4f2;
    --backdrop: #ededed;
    --white: #ffffff;
  }
  * { box-sizing: border-box; margin: 0; padding: 0; }
  html, body {
    width: 1200px; height: 800px; overflow: hidden;
    background: var(--backdrop);
    font-family: "Open Sans", Arial, sans-serif;
    color: var(--ink);
  }
  .card-set { position: relative; width: 1200px; height: 800px; }
  .card {
    position: absolute;
    width: 360px; height: 236px;
    border-radius: 3px;
    box-shadow: 0 6px 14px rgba(0,0,0,0.12);
    overflow: hidden;
  }
  .card--front { left: 330px; top: 36px; background: var(--paper); }
  .card--back-blue { left: 420px; top: 290px; background: var(--brand-blue); }
  .card--back-white { left: 510px; top: 544px; background: var(--paper); height: 220px; }

  /* front */
  .front__stripe { position: absolute; left: 0; top: 0; bottom: 0; width: 9px; background: var(--brand-blue); }
  .front__details { position: absolute; left: 34px; top: 40px; font-size: 9.5px; line-height: 1.45; color: var(--ink-soft); }
  .front__name { font-size: 12.5px; font-weight: 700; color: var(--ink); letter-spacing: 0.3px; }
  .front__title { font-weight: 400; font-size: 10.5px; margin-left: 6px; }
  .contact-list { margin-top: 8px; list-style: none; }
  .contact-list .label { display: inline-block; width: 14px; color: var(--brand-blue); font-weight: 600; }
  .address { margin-top: 10px; }
  .social-list { margin-top: 10px; list-style: none; }
  .social-list li { display: flex; align-items: center; gap: 8px; margin-bottom: 2px; }
  .social-dot { width: 10px; height: 10px; border-radius: 50%; background: var(--brand-blue); }
  .front__brand { position: absolute; right: 24px; top: 128px; }

  /* wordmark */
  .wordmark { display: flex; align-items: center; gap: 7px; font-weight: 600; color: var(--ink); white-space: nowrap; }
  .wordmark__dot { background: var(--brand-blue); }
  .wordmark--small { font-size: 15px; }
  .wordmark--small .wordmark__dot { width: 9px; height: 9px; }
  .wordmark--large { font-size: 27px; justify-content: center; }
  .wordmark--large .wordmark__dot { width: 13px; height: 13px; }
  .wordmark--on-blue .wordmark__dot { background: var(--ink); }

  /* blue back */
  .back-blue__brand { position: absolute; left: 0; right: 0; top: 78px; }
  .back-blue__rule { position: absolute; left: 95px; right: 95px; top: 150px; height: 1px; background: rgba(255,255,255,0.75); }
  .back-blue__url { position: absolute; left: 0; right: 0; top: 160px; text-align: center; color: var(--white); font-size: 10.5px; letter-spacing: 0.3px; }

  /* white back */
  .back-white__brand { position: absolute; left: 0; right: 0; top: 70px; }
  .back-white__band { position: absolute; left: 0; right: 0; bottom: 24px; height: 36px; background: var(--brand-blue);
    display: flex; align-items: center; justify-content: center; color: var(--white); font-size: 10.5px; letter-spacing: 0.3px; }
</style>
</head>
<body>
<main class="card-set">

  <section class="card card--front" aria-label="Card front">
    <div class="front__stripe"></div>
    <div class="front__details">
      <p><span class="front__name">DENNIS HALVORSEN</span><span class="front__title">Owner</span></p>
      <ul class="contact-list">
        <li><span class="label">T</span>1.888.555.0162</li>
        <li><span class="label">E</span>dennis.h@corvantsys.example</li>
      </ul>
      <p class="address">512 Brindlemoor Rd Unit C<br>Ashford Vale, NH 02871</p>
      <ul class="social-list">
        <li><span class="social-dot"></span>/CorvantSys</li>
        <li><span class="social-dot"></span>/corvantsys</li>
        <li><span class="social-dot"></span>/corvantsys/</li>
      </ul>
    </div>
    <div class="front__brand wordmark wordmark--small"><span class="wordmark__dot"></span>Corvant Systems</div>
  </section>

  <section class="card card--back-blue" aria-label="Card back, blue">
    <div class="back-blue__brand wordmark wordmark--large wordmark--on-blue"><span class="wordmark__dot"></span>Corvant Systems</div>
    <div class="back-blue__rule"></div>
    <p class="back-blue__url">www.corvantsys.example</p>
  </section>

  <section class="card card--back-white" aria-label="Card back, white">
    <div class="back-white__brand wordmark wordmark--large"><span class="wordmark__dot"></span>Corvant Systems</div>
    <div class="back-white__band">www.corvantsys.example</div>
  </section>

</main>
</body>
</html>
```